Label Design for Sacha Inchi Oil in 250ml Bottle

We need unique labeling design for our product, Sacha Inchi Oil in 250ml glass bottle form. The final design should have the Company logo and the product label ORN'S displayed. We have attached the artwork of our Company logo and the nutrients/consumption details of the product for your necessary designing. Label size for the 250ml bottle will be 122mm x 34mm.

It Company

```html
<!DOCTYPE html>
<html lang="en">
<head>
<meta charset="utf-8">
<title>ORN'S Cold Pressed Sacha Inchi Oil – 250ml Label</title>
<link rel="stylesheet" href="https://fonts.googleapis.com/css2?family=Libre+Baskerville:wght@700&family=Cormorant+Garamond:ital,wght@1,700&family=Arimo:wght@500&display=swap">
<style>
  :root {
    --canvas-bg: #ffffff;
    --label-cream-light: #ecebc0;
    --label-cream-dark: #d8d49a;
    --bark-brown: #3b2a1c;
    --bark-brown-line: #6b4d33;
    --leaf-green: #1e7a3c;
    --leaf-green-dark: #146530;
    --title-brown: #3a2a1d;
    --tab-white: #f6f4e4;
  }
  html, body {
    margin: 0;
    padding: 0;
    width: 1200px;
    height: 1200px;
    overflow: hidden;
    background: var(--canvas-bg);
  }
  .label {
    position: absolute;
    left: 210px;
    top: 105px;
    width: 780px;
    height: 990px;
  }
  .brand-title {
    font-family: "Libre Baskerville", "Times New Roman", serif;
    font-weight: 700;
    fill: var(--title-brown);
  }
  .product-line {
    font-family: "Cormorant Garamond", Georgia, serif;
    font-style: italic;
    font-weight: 700;
    fill: var(--leaf-green);
  }
  .company-name {
    font-family: "Libre Baskerville", "Times New Roman", serif;
    font-weight: 700;
    fill: var(--leaf-green);
    letter-spacing: 6px;
  }
  .purity-value, .purity-words {
    font-family: "Libre Baskerville", "Times New Roman", serif;
    font-weight: 700;
    fill: var(--tab-white);
  }
  .volume {
    font-family: "Arimo", Arial, sans-serif;
    font-weight: 500;
    fill: #2a2118;
  }
</style>
</head>
<body>
<svg class="label" viewBox="0 0 780 990" xmlns="http://www.w3.org/2000/svg">
  <defs>
    <linearGradient id="cream-field" x1="0" y1="0" x2="1" y2="0">
      <stop offset="0" stop-color="var(--label-cream-dark)"/>
      <stop offset="0.5" stop-color="var(--label-cream-light)"/>
      <stop offset="1" stop-color="var(--label-cream-dark)"/>
    </linearGradient>
  </defs>

  <!-- label field -->
  <rect class="label-field" x="0" y="0" width="780" height="990" fill="url(#cream-field)" role="img" aria-label="Soft cream background with faint leaf pattern"/>

  <!-- top border band -->
  <rect class="top-band" x="0" y="0" width="780" height="27" fill="var(--bark-brown)"/>
  <line x1="0" y1="20" x2="780" y2="20" stroke="var(--bark-brown-line)" stroke-width="2"/>

  <!-- corner tabs -->
  <path class="corner-tab" d="M0 90 H115 Q147 90 147 122 V500" fill="none" stroke="var(--leaf-green)" stroke-width="3"/>
  <path class="corner-tab" d="M780 90 H652 Q620 90 620 122 V500" fill="none" stroke="var(--leaf-green)" stroke-width="3"/>

  <!-- company mark frame -->
  <path class="mark-frame" d="M147 27 V240 Q147 269 176 269 H591 Q620 269 620 240 V27" fill="var(--label-cream-light)" stroke="var(--leaf-green)" stroke-width="3"/>
  <circle cx="278" cy="148" r="22" fill="none" stroke="var(--leaf-green)" stroke-width="4"/>
  <text class="company-name" x="414" y="163" font-size="42" text-anchor="middle">TANARA</text>

  <!-- brand name -->
  <text class="brand-title" x="390" y="470" font-size="150" text-anchor="middle">ORN'S</text>

  <!-- product description -->
  <text class="product-line" x="390" y="570" font-size="60" text-anchor="middle">Cold Pressed Sacha Inchi Oil</text>
  <text class="product-line" x="390" y="638" font-size="60" text-anchor="middle">Minyak Sacha Inchi Perahan Sejuk</text>

  <!-- green band with purity tab -->
  <rect class="green-band" x="0" y="848" width="780" height="84" fill="var(--leaf-green)"/>
  <path class="purity-tab" d="M147 932 V760 Q147 730 177 730 H590 Q620 730 620 760 V932 Z" fill="var(--leaf-green)"/>
  <text class="purity-value" x="384" y="820" font-size="72" text-anchor="middle">100%</text>
  <text class="purity-words" x="384" y="908" font-size="56" text-anchor="middle">PURE ASLI</text>

  <text class="volume" x="712" y="815" font-size="50" text-anchor="middle">250ml</text>

  <!-- bottom border band -->
  <rect class="bottom-band" x="0" y="932" width="780" height="58" fill="var(--bark-brown)"/>
  <line x1="0" y1="944" x2="780" y2="944" stroke="var(--bark-brown-line)" stroke-width="2"/>
  <line x1="0" y1="978" x2="780" y2="978" stroke="var(--bark-brown-line)" stroke-width="2"/>
</svg>
</body>
</html>
```